LWB Homepage Banner

I would like a banner that uses/interprets the existing graphic on the www.leonwardbriggs.example homepage.

Target Market(s)

Business professionals across a variety of industries and sectors.

Requirements
Must have
• Must incorporate all the words and relationships of the existing image (file attached). I am seeking a professional and clean interpretation of the image.
• Must consider the look and feel of the banner on the following page: http://www.leonwardbriggs.example/pathways-in-coastal-crm/ (file attached)
• Must include the LWB logo in a similar style to the banner on the Pathways in Coastal CRM page (file attached).
Nice to have
• Feel free to add background/foreground graphics.
• I like the design idea of "bio-mechanical" applied to a professional services/business industry.
• The overall image must display a "business-technology-people-change" balance.
Should not have
• Should not be a direct replication of the existing graphic but must contain all the words and relationships.

```html
<!DOCTYPE html>
<html lang="en">
<head>
<meta charset="utf-8">
<title>LWB Homepage Banner</title>
<link rel="stylesheet" href="https://fonts.googleapis.com/css2?family=Source+Sans+3:wght@400;600;700;800&family=EB+Garamond:wght@500&display=swap">
<style>
  :root {
    --sky-top: #3aa6e0;
    --sky-mid: #1b6fb4;
    --sky-deep: #0b2d63;
    --navy: #23338f;
    --navy-ring: #1d1f6e;
    --orange: #e8922e;
    --silver-light: #f4f5f6;
    --silver-mid: #c9cdd1;
    --silver-dark: #8d949b;
    --ink: #1c1d20;
    --brand-blue: #1f4f96;
    --white: #ffffff;
  }
  html, body {
    margin: 0;
    padding: 0;
    width: 1200px;
    height: 513px;
    overflow: hidden;
    background: var(--white);
  }
  .banner {
    display: block;
    width: 1200px;
    height: 513px;
  }
  .title {
    font-family: "Source Sans 3", Arial, sans-serif;
    font-weight: 800;
    font-size: 24px;
  }
  .tagline {
    font-family: "Source Sans 3", Arial, sans-serif;
    font-weight: 700;
    font-size: 11.5px;
  }
  .on-dark { fill: var(--white); }
  .on-silver { fill: var(--ink); }
  .gear-label {
    font-family: "Source Sans 3", Arial, sans-serif;
    font-weight: 800;
    font-size: 12.5px;
    fill: var(--ink);
    letter-spacing: 0.4px;
  }
  .gear-hub-label {
    font-family: "Source Sans 3", Arial, sans-serif;
    font-weight: 800;
    font-size: 15px;
    fill: var(--ink);
    letter-spacing: 0.4px;
  }
  .role-label {
    font-family: "Source Sans 3", Arial, sans-serif;
    font-weight: 600;
    font-size: 11.5px;
    fill: var(--ink);
  }
  .brand-name {
    font-family: "Source Sans 3", Arial, sans-serif;
    font-weight: 700;
    font-size: 22px;
    fill: var(--brand-blue);
  }
  .mission {
    font-family: "EB Garamond", Georgia, serif;
    font-weight: 500;
    font-size: 15.5px;
    fill: var(--brand-blue);
  }
</style>
</head>
<body>
<svg class="banner" viewBox="0 0 1200 513" xmlns="http://www.w3.org/2000/svg">
  <defs>
    <linearGradient id="sky" x1="0" y1="0" x2="0.3" y2="1">
      <stop offset="0" stop-color="#3aa6e0"/>
      <stop offset="0.55" stop-color="#1b6fb4"/>
      <stop offset="1" stop-color="#0b2d63"/>
    </linearGradient>
    <radialGradient id="metal" cx="0.4" cy="0.35" r="0.7">
      <stop offset="0" stop-color="#f4f5f6"/>
      <stop offset="0.6" stop-color="#c9cdd1"/>
      <stop offset="1" stop-color="#8d949b"/>
    </radialGradient>
    <linearGradient id="plate" x1="0" y1="0" x2="0" y2="1">
      <stop offset="0" stop-color="#f4f5f6"/>
      <stop offset="1" stop-color="#c9cdd1"/>
    </linearGradient>
  </defs>

  <rect class="backdrop" x="20" y="10" width="1180" height="487" fill="url(#sky)"/>
  <g class="circuit-lines" stroke="#7fd0ff" stroke-opacity="0.25" fill="none" stroke-width="1">
    <path d="M20 150 H140 V220 H170"/>
    <path d="M1040 120 H1120 V200 H1200"/>
    <path d="M120 400 H160 V360"/>
    <path d="M1060 380 H1150 V330"/>
  </g>

  <g class="heading heading--procurement">
    <polygon points="205,38 450,38 470,86 205,86" fill="var(--navy)"/>
    <text class="title on-dark" x="312" y="63" text-anchor="middle">PROCURMENT RISK</text>
    <text class="tagline on-dark" x="312" y="79" text-anchor="middle">The right partner</text>
  </g>
  <g class="heading heading--independence">
    <polygon points="440,20 775,20 750,66 465,66" fill="url(#plate)"/>
    <text class="title on-silver" x="607" y="45" text-anchor="middle">INDEPENDENCE RISK</text>
    <text class="tagline on-silver" x="607" y="60" text-anchor="middle">The right technology framework</text>
    <line x1="480" y1="85" x2="735" y2="85" stroke="var(--white)" stroke-width="2"/>
  </g>
  <g class="heading heading--business">
    <polygon points="770,38 1015,38 1015,86 750,86" fill="var(--orange)"/>
    <text class="title on-dark" x="882" y="63" text-anchor="middle">BUSINESS RISK</text>
    <text class="tagline on-dark" x="882" y="79" text-anchor="middle">The right outcome</text>
  </g>

  <g class="gear gear--procurement">
    <circle cx="306" cy="255" r="142" fill="url(#metal)" role="img" aria-label="Metallic gear for the procurement cycle"/>
    <circle cx="306" cy="255" r="102" fill="none" stroke="var(--navy-ring)" stroke-width="5"/>
    <text class="gear-label" transform="translate(314,190) rotate(-80)" text-anchor="middle">PROCURE</text>
    <text class="gear-label" transform="translate(252,240) rotate(18)" text-anchor="middle">EVALUATE</text>
    <text class="gear-label" transform="translate(362,246) rotate(-22)" text-anchor="middle">IMPLEMENT</text>
    <text class="gear-label" transform="translate(268,312) rotate(68)" text-anchor="middle">UPGRADE</text>
    <text class="gear-label" transform="translate(350,312) rotate(55)" text-anchor="middle">MAINTAIN</text>
  </g>

  <g class="gear gear--business">
    <circle cx="868" cy="255" r="142" fill="url(#metal)" role="img" aria-label="Metallic gear for the business change cycle"/>
    <circle cx="868" cy="255" r="102" fill="none" stroke="var(--orange)" stroke-width="5"/>
    <text class="gear-label" transform="translate(866,192) rotate(90)" text-anchor="middle">IMPLEMENT</text>
    <text class="gear-label" transform="translate(914,246) rotate(-20)" text-anchor="middle">GOVERN</text>
    <text class="gear-label" transform="translate(822,236) rotate(200)" text-anchor="middle">PROCESS</text>
    <text class="gear-label" transform="translate(840,312) rotate(-64)" text-anchor="middle">COMMUNICATE</text>
    <text class="gear-label" transform="translate(900,304) rotate(60)" text-anchor="middle">CHANGE</text>
  </g>

  <g class="gear gear--enterprise">
    <circle cx="588" cy="282" r="128" fill="url(#metal)" role="img" aria-label="Metallic gear for the enterprise technology framework"/>
    <circle cx="588" cy="282" r="95" fill="none" stroke="var(--silver-dark)" stroke-width="3"/>
    <text class="gear-label" x="590" y="188" text-anchor="middle">STRATEGY</text>
    <text class="gear-label" transform="translate(672,236) rotate(60)" text-anchor="middle">SOFTWARE</text>
    <text class="gear-label" transform="translate(672,336) rotate(-60)" text-anchor="middle">HARDWARE</text>
    <text class="gear-label" transform="translate(506,338) rotate(60)" text-anchor="middle">NETWORKS</text>
    <text class="gear-label" transform="translate(506,236) rotate(-60)" text-anchor="middle">SERVICES</text>
    <text class="gear-hub-label" transform="translate(590,276) rotate(45)" text-anchor="middle">ENTERPRISE</text>
  </g>

  <g class="roles">
    <polygon points="532,431 640,431 632,448 540,448" fill="url(#plate)"/>
    <text class="role-label" x="586" y="444" text-anchor="middle">Analysts</text>
    <polygon points="532,451 640,451 632,468 540,468" fill="url(#plate)"/>
    <text class="role-label" x="586" y="464" text-anchor="middle">Advisors</text>
    <polygon points="525,471 647,471 639,488 533,488" fill="url(#plate)"/>
    <text class="role-label" x="586" y="484" text-anchor="middle">Program Managers</text>
  </g>

  <g class="brand">
    <rect x="20" y="429" width="284" height="58" fill="var(--white)"/>
    <rect x="40" y="449" width="18" height="18" fill="var(--brand-blue)"/>
    <text class="brand-name" x="70" y="466">Leon Ward Briggs</text>
  </g>

  <g class="mission-block">
    <rect x="895" y="425" width="290" height="60" fill="var(--white)"/>
    <text class="mission" x="1040" y="449" text-anchor="middle">Supporting Organisational Technology</text>
    <text class="mission" x="1040" y="470" text-anchor="middle">Risk Management Outcomes</text>
  </g>
</svg>
</body>
</html>
```